Lantern Group - Tax season post card

We need postcard designed for a service firm, The Lantern Group LLC primarily for the tax season and also to promote our other service areas. We would like the use of our logo and prefer the orange, green, white color combinations but also open to suggestions. Use the three logos from the attached tax alert flyerThe Lantern Group is one stop shop for all your accounting, finance and compliance needs. The firm provides the following services-Accounting & BookkeepingBusiness Advisory Immigration Consulting Income tax preparationIRS RepresentationNon-profit AuditsNotary PublicPayroll and Sales taxLive-Scan fingerprintingProperty ManagementRetirement PlanningThe firm is managed by highly qualified and experienced CPA's, Enrolled Agents, and California Certified Tax Professionals. We give 25% discount for the first time client utilizing our accounting & book-keeping, audit services from your prior year CPA's fees.For the tax season we have $50 discount for our first time clientsTax preparation and consulting include, Trusts, Estates, S-Corp, C-Corp, Partnership, Non-Profit, and Individual Returns2605 Pacific AvenueStockton, CA 95204Phone: 209.463.4436Email: marel.lanterngroup@quillmail.net

Target Market(s)

Businesses and individuals looking for accountant

Industry/Entity Type

Accounting

Font styles to use
Serif

Colors
ec1f27
f37122
ffcf3e

Requirements
Must have
• All services listed
Nice to have
• Attractive logo and fonts
Should not have
• clutter. Too much content tightly adjusted

```html
<!DOCTYPE html>
<html lang="en">
<head>
<meta charset="utf-8">
<title>Lantern Group – Tax Season Postcard</title>
<link href="https://fonts.googleapis.com/css2?family=Questrial&display=swap" rel="stylesheet">
<style>
  :root {
    --green: #079a48;
    --orange: #ef6a32;
    --white: #ffffff;
    --ink: #2a2a2a;
    --backdrop: #2b2b2b;
    --photo-light: #dcdde0;
    --photo-mid: #9fa6b0;
    --photo-dark: #2e3442;
  }
  * { margin: 0; padding: 0; box-sizing: border-box; }
  html, body { width: 900px; height: 1200px; overflow: hidden; }
  body {
    background: var(--backdrop);
    font-family: "Questrial", "Century Gothic", sans-serif;
    position: relative;
  }
  .postcard {
    position: absolute;
    left: 143px;
    width: 640px;
    background: var(--white);
    overflow: hidden;
  }
  .postcard--front { top: 82px; height: 491px; }
  .postcard--back { top: 613px; height: 492px; }
  .shapes { position: absolute; inset: 0; }

  .hero-photo {
    position: absolute;
    inset: 0;
    background: linear-gradient(160deg, var(--photo-light) 0%, var(--photo-light) 30%, var(--photo-mid) 55%, var(--photo-dark) 75%, var(--photo-light) 95%);
    clip-path: polygon(0 0, 427px 0, 279px 491px, 0 491px);
  }

  .offer-badge {
    position: absolute;
    left: 205px; top: 328px;
    width: 146px; height: 146px;
    border-radius: 50%;
    background: var(--white);
    text-align: center;
    color: var(--ink);
    padding-top: 14px;
  }
  .offer-badge__value { color: var(--orange); font-size: 39px; line-height: 40px; }
  .offer-badge__text { font-size: 20.5px; line-height: 27px; }

  .services {
    position: absolute;
    left: 382px; top: 156px;
    color: var(--ink);
  }
  .services__title {
    color: var(--white);
    font-size: 25px;
    font-weight: 400;
    margin-left: 19px;
    padding-bottom: 2px;
    border-bottom: 2px solid var(--white);
    width: 192px;
    margin-bottom: 6px;
  }
  .services__list { list-style: none; font-size: 19.5px; line-height: 22.9px; }
  .services__list li::before { content: "•"; margin-right: 3px; }

  .brand {
    position: absolute;
    left: 15px; top: 24px;
    display: flex; align-items: center; gap: 10px;
    color: var(--white);
    font-size: 24px;
  }
  .brand__mark {
    width: 26px; height: 26px;
    border-radius: 50%;
    background: var(--orange);
  }

  .tag {
    position: absolute;
    background: var(--orange);
    color: var(--white);
    font-size: 24px;
    padding-left: 13px;
    width: 185px; height: 33px;
    line-height: 34px;
  }
  .tag--about { left: 15px; top: 81px; }
  .tag--contact { left: 20px; top: 225px; }
  .about-text {
    position: absolute;
    left: 14px; top: 131px;
    color: var(--white);
    font-size: 17.5px;
    line-height: 22px;
  }
  .contact {
    position: absolute;
    left: 9px; top: 268px;
    color: var(--white);
    font-size: 19px;
    line-height: 23px;
  }
  .contact__address { padding-left: 20px; margin-bottom: 2px; }
  .contact__row { display: flex; align-items: center; gap: 3px; }
  .contact__row svg { flex: none; }

  .tax-offer {
    position: absolute;
    left: 15px; top: 404px;
    width: 300px;
    color: var(--white);
    font-size: 17.5px;
    line-height: 23px;
  }
  .tax-offer__value { color: var(--white); background: var(--orange); padding: 0 6px; }
</style>
</head>
<body>

<section class="postcard postcard--front">
  <div class="hero-photo" role="img" aria-label="Photo of a smiling accountant at a desk working with a calculator and paperwork"></div>
  <svg class="shapes" width="640" height="491" viewBox="0 0 640 491" aria-hidden="true">
    <polygon points="427,0 442,0 289,491 279,491" fill="var(--orange)"/>
    <polygon points="442,0 640,0 640,491 289,491" fill="var(--green)"/>
  </svg>
  <div class="offer-badge">
    <div class="offer-badge__value">25%</div>
    <div class="offer-badge__text">discount for<br>the first time<br>client</div>
  </div>
  <div class="services">
    <h2 class="services__title">Our Services:</h2>
    <ul class="services__list">
      <li>Accounting</li>
      <li>Bookkeeping</li>
      <li>Business Advisory</li>
      <li>Immigration Consulting</li>
      <li>Income tax preparation</li>
      <li>IRS Representation</li>
      <li>Non-profit Audits</li>
      <li>Notary Public</li>
      <li>Payroll and Sales tax</li>
      <li>Live-Scan fingerprinting</li>
      <li>Property Management</li>
      <li>Retirement Planning</li>
    </ul>
  </div>
</section>

<section class="postcard postcard--back">
  <svg class="shapes" width="640" height="492" viewBox="0 0 640 492" aria-hidden="true">
    <polygon points="0,0 400,0 297,492 0,492" fill="var(--green)"/>
    <polygon points="400,0 414,0 309,492 297,492" fill="var(--orange)"/>
    <rect x="533.5" y="23.5" width="82" height="74" fill="none" stroke="#333" stroke-width="1"/>
    <line x1="369" y1="277" x2="625" y2="277" stroke="#444" stroke-width="1"/>
    <line x1="369" y1="322" x2="625" y2="322" stroke="#444" stroke-width="1"/>
    <line x1="369" y1="365" x2="625" y2="365" stroke="#444" stroke-width="1"/>
  </svg>
  <div class="brand">
    <span class="brand__mark" aria-hidden="true"></span>
    <span class="brand__name">The Lantern Group LLC</span>
  </div>
  <div class="tag tag--about">About Us:</div>
  <p class="about-text">The firm is managed by highly qualified<br>and experienced CPA's, Enrolled Agents,<br>and California Certified Tax Professionals.</p>
  <div class="tag tag--contact">Contact Us:</div>
  <div class="contact">
    <p class="contact__address">4718 Birchwood Avenue<br>Stockton, CA 95204</p>
    <p class="contact__row">
      <svg width="16" height="16" viewBox="0 0 16 16" aria-hidden="true"><circle cx="8" cy="8" r="7" fill="none" stroke="#fff" stroke-width="1"/><path d="M6 4.5 L7.5 6.5 L6.8 7.5 Q7.5 9 8.8 9.8 L9.8 9 L11.5 10.8 L10.5 12 Q7 11.5 5 7 Z" fill="#fff"/></svg>
      <span>209.555.0187</span>
    </p>
    <p class="contact__row">
      <svg width="16" height="12" viewBox="0 0 16 12" aria-hidden="true"><rect x="0.5" y="0.5" width="15" height="11" fill="none" stroke="#fff"/><path d="M0.5 0.5 L8 7 L15.5 0.5" fill="none" stroke="#fff"/></svg>
      <span>marel.lanterngroup@quillmail.net</span>
    </p>
  </div>
  <p class="tax-offer">Tax season: <span class="tax-offer__value">$50 off</span><br>for first time clients</p>
</section>

</body>
</html>
```